kestrelnet9 - a safety solution for schools

A Amok App for schools needs your help to design some screens. Its important to have a very simple use of the app. The function of the app is very easy, you put the button to trigger the alarm. The app has a message function. So we need 3 howto screens. you find a better description of the project in the briefing-file. If you have any questions just ask. Thanks in advance for the suggestions. Best Regards, Lars

Target Market(s)

Schools

Industry/Entity Type

Security Service

Font styles to use
Sans Serif

Colors

Designer to choose colors to be used in the design.

Requirements
Must have
• Simple, easy to use, look like a security app, trust,

```html
<!DOCTYPE html>
<html lang="de">
<head>
<meta charset="utf-8">
<title>kestrelnet9 – Schul-Alarm</title>
<link rel="stylesheet" href="https://fonts.googleapis.com/css2?family=Roboto:wght@400;500;700&display=swap">
<style>
  :root {
    --backdrop: #6c6fcc;
    --screen: #ffffff;
    --ink: #2e2e2e;
    --band-blue: #1f5fcf;
    --alarm-red: #cf3135;
    --ring-grey: #ebebeb;
    --chat-orange: #e99c2a;
    --settings-blue: #1ea1e8;
    --white: #ffffff;
  }
  html, body {
    margin: 0;
    padding: 0;
    width: 1200px;
    height: 1200px;
    overflow: hidden;
    background: var(--backdrop);
    font-family: "Roboto", Arial, sans-serif;
  }
  .app-screen {
    position: absolute;
    left: 264px;
    top: 0;
    width: 672px;
    height: 1200px;
    background: var(--screen);
    overflow: hidden;
  }
  .message-banner {
    position: absolute;
    left: 0; top: 0;
    width: 100%;
    height: 94px;
    background: var(--white);
    display: flex;
    align-items: center;
    z-index: 2;
  }
  .message-banner .banner-icon {
    position: absolute;
    left: 16px;
    top: 22px;
    width: 54px;
    height: 54px;
  }
  .message-banner .banner-text {
    position: absolute;
    left: 93px;
    top: 33px;
    font-size: 25px;
    line-height: 30px;
    color: var(--ink);
    white-space: nowrap;
  }
  .banner-text strong { font-weight: 700; }
  .header-band {
    position: absolute;
    left: 0; top: 94px;
    width: 100%;
    height: 27px;
    background: var(--band-blue);
  }
  .screen-title {
    position: absolute;
    left: 0; top: 242px;
    width: 100%;
    text-align: center;
    font-size: 33px;
    font-weight: 700;
    letter-spacing: 0.2px;
    color: var(--ink);
    margin: 0;
  }
  .alarm-button {
    position: absolute;
    left: 126px;
    top: 360px;
    width: 420px;
    height: 420px;
    border-radius: 50%;
    background: var(--ring-grey);
    display: flex;
    align-items: center;
    justify-content: center;
  }
  .alarm-button .alarm-core {
    width: 384px;
    height: 384px;
    border-radius: 50%;
    background: var(--alarm-red);
    display: flex;
    align-items: center;
    justify-content: center;
  }
  .alarm-core .brand-name {
    font-size: 36px;
    font-weight: 500;
    color: var(--white);
  }
  .fab {
    position: absolute;
    top: 1025px;
    width: 104px;
    height: 104px;
    border-radius: 50%;
    box-shadow: 0 4px 8px rgba(0,0,0,0.18);
    display: flex;
    align-items: center;
    justify-content: center;
  }
  .fab-chat { left: 47px; background: var(--chat-orange); }
  .fab-settings { left: 522px; background: var(--settings-blue); }
  .fab svg { width: 56px; height: 56px; }
</style>
</head>
<body>
  <main class="app-screen">
    <div class="message-banner">
      <svg class="banner-icon" viewBox="0 0 54 54" aria-hidden="true">
        <circle cx="27" cy="27" r="27" fill="var(--chat-orange)"/>
        <ellipse cx="27" cy="26" rx="14" ry="11" fill="#fff"/>
        <path d="M17 32 L14 40 L23 35 Z" fill="#fff"/>
        <circle cx="21" cy="26" r="2" fill="var(--chat-orange)"/>
        <circle cx="27" cy="26" r="2" fill="var(--chat-orange)"/>
        <circle cx="33" cy="26" r="2" fill="var(--chat-orange)"/>
      </svg>
      <div class="banner-text"><strong>Sekretariat:</strong> Bitte bleiben Sie wo Sie sind</div>
    </div>
    <div class="header-band"></div>

    <h1 class="screen-title">SCHUL-ALARM AUSLÖSEN</h1>

    <div class="alarm-button">
      <div class="alarm-core">
        <span class="brand-name">kestrelnet9</span>
      </div>
    </div>

    <div class="fab fab-chat">
      <svg viewBox="0 0 56 56" aria-label="Nachrichten">
        <ellipse cx="29" cy="26" rx="22" ry="17" fill="#fff"/>
        <path d="M13 36 L8 49 L24 41 Z" fill="#fff"/>
        <circle cx="20" cy="26" r="3" fill="var(--chat-orange)"/>
        <circle cx="29" cy="26" r="3" fill="var(--chat-orange)"/>
        <circle cx="38" cy="26" r="3" fill="var(--chat-orange)"/>
      </svg>
    </div>

    <div class="fab fab-settings">
      <svg viewBox="0 0 56 56" aria-label="Einstellungen">
        <g fill="#fff" transform="translate(28 28)">
          <rect x="-5" y="-22" width="10" height="10" rx="2"/>
          <rect x="-5" y="-22" width="10" height="10" rx="2" transform="rotate(45)"/>
          <rect x="-5" y="-22" width="10" height="10" rx="2" transform="rotate(90)"/>
          <rect x="-5" y="-22" width="10" height="10" rx="2" transform="rotate(135)"/>
          <rect x="-5" y="-22" width="10" height="10" rx="2" transform="rotate(180)"/>
          <rect x="-5" y="-22" width="10" height="10" rx="2" transform="rotate(225)"/>
          <rect x="-5" y="-22" width="10" height="10" rx="2" transform="rotate(270)"/>
          <rect x="-5" y="-22" width="10" height="10" rx="2" transform="rotate(315)"/>
          <circle r="15"/>
        </g>
        <circle cx="28" cy="28" r="6" fill="var(--settings-blue)"/>
      </svg>
    </div>
  </main>
</body>
</html>
```